Brenvik Innovations
Professional
Daniel Marlow
CEO
5812-4 Calloway Ave #2267
Houston, TX 77194
Daniel@BrenvikInnovations.com
BrenvikInnovations.com
Feel free to play with the function of the business card if possible as seen in: http://www.trelvaform-studio.com/blog/wp-content/uploads/2009/12/lock-picking-business-card.jpg. Card can be paper plastic or metal.
Our company specializes in artificial intelligence, Unmanned aerial vehicles human-machine interfaces and lasers. Please keep this in mind in your designs.
surprise me, I will refine my requirement here after I see a few submissions.
Here are the business logo files

```html
<!DOCTYPE html>
<html lang="en">
<head>
<meta charset="utf-8">
<title>Brenvik Innovations — Stationery</title>
<link href="https://fonts.googleapis.com/css2?family=Arimo:wght@400;700&display=swap" rel="stylesheet">
<style>
  :root {
    --purple: #3a3585;
    --purple-deep: #2b2768;
    --grey: #b8b8c4;
    --grey-light: #e4e4ea;
    --paper: #ffffff;
    --ink: #4a4a55;
    --name-red: #b3344a;
    --stage: #f2f2f4;
  }
  * { margin: 0; padding: 0; box-sizing: border-box; }
  html, body { width: 1200px; height: 935px; overflow: hidden; }
  body {
    position: relative;
    background: var(--paper);
    font-family: "Arimo", Arial, sans-serif;
    color: var(--ink);
  }
  .sheet {
    position: absolute;
    background: var(--paper);
    box-shadow: 0 1px 4px rgba(0,0,0,.25);
    overflow: hidden;
  }
  .brand {
    display: flex;
    align-items: center;
    gap: 6px;
    font-weight: 700;
    color: var(--purple);
    text-transform: uppercase;
    line-height: 1;
    letter-spacing: .02em;
  }
  .brand-mark { background: var(--purple); flex: none; }
  .wave { position: absolute; left: 0; bottom: 0; width: 100%; display: block; }

  /* business cards */
  .card { top: 0; width: 278px; height: 203px; background: var(--stage); }
  .card-front { left: 38px; }
  .card-back { left: 337px; }
  .card-front .brand { position: absolute; left: 20px; top: 22px; font-size: 13px; }
  .card-front .brand-mark { width: 12px; height: 12px; }
  .card-contact { position: absolute; left: 20px; top: 62px; font-size: 8.5px; line-height: 1.45; }
  .card-contact .person { color: var(--name-red); font-size: 12px; }
  .card-contact .role { color: var(--name-red); margin-bottom: 8px; }
  .card-back .brand { position: absolute; right: 22px; top: 40px; font-size: 15px; color: var(--grey); }
  .card-back .brand-mark { width: 14px; height: 14px; background: var(--grey); }

  /* envelope */
  .envelope { left: 653px; top: 0; width: 532px; height: 410px; }
  .envelope-flap {
    position: absolute; left: 0; top: 0; width: 100%; height: 75px;
    background: linear-gradient(#ffffff, var(--grey-light) 60%, var(--grey));
    display: flex; justify-content: center; align-items: center;
  }
  .envelope-flap .brand-mark { width: 18px; height: 18px; }
  .envelope-band {
    position: absolute; left: 0; top: 75px; width: 100%; height: 90px;
    background: var(--purple);
    display: flex; justify-content: center; align-items: center;
  }
  .envelope-band .brand-mark { width: 18px; height: 18px; background: #6f6ab2; }
  .envelope .brand.return { position: absolute; left: 18px; top: 180px; font-size: 19px; }
  .envelope .brand.return .brand-mark { width: 16px; height: 16px; }
  .return-address { position: absolute; left: 22px; top: 318px; font-size: 7px; line-height: 1.4; }

  /* letterhead */
  .letterhead { left: 5px; top: 261px; width: 471px; height: 662px; }
  .letterhead .brand { position: absolute; left: 14px; top: 16px; font-size: 17px; }
  .letterhead .brand-mark { width: 16px; height: 16px; }
  .letter-contact {
    position: absolute; right: 40px; top: 20px;
    font-size: 6.5px; line-height: 1.45;
    display: grid; grid-template-columns: auto auto; column-gap: 10px;
  }

  /* continuation sheets */
  .note { top: 460px; width: 336px; height: 463px; }
  .note-a { left: 498px; }
  .note-b { left: 862px; }
  .note-header {
    position: absolute; left: 14px; right: 14px; top: 12px;
    display: flex; justify-content: space-between; align-items: flex-end;
    padding-bottom: 4px; border-bottom: 1px solid var(--grey);
  }
  .note-header .brand { font-size: 13px; }
  .note-header .brand-mark { width: 12px; height: 12px; }
  .note-owner { font-size: 8px; color: #8a8a96; }
</style>
</head>
<body>

  <section class="sheet card card-front">
    <div class="brand"><span class="brand-mark"></span>Brenvik Innovations</div>
    <div class="card-contact">
      <div class="person">Daniel Marlow</div>
      <div class="role">CEO</div>
      <div>5812-4 Calloway Ave #2267</div>
      <div>Houston, TX 77194</div>
      <div>Phone: 713.555.0148</div>
      <div>Daniel@BrenvikInnovations.com</div>
      <div>BrenvikInnovations.com</div>
    </div>
  </section>

  <section class="sheet card card-back">
    <div class="brand"><span class="brand-mark"></span>Brenvik Innovations</div>
  </section>

  <section class="sheet envelope">
    <div class="envelope-flap"><span class="brand-mark"></span></div>
    <div class="envelope-band"><span class="brand-mark"></span></div>
    <div class="brand return"><span class="brand-mark"></span>Brenvik Innovations</div>
    <div class="return-address">
      <div>5812-4 Calloway Ave #2267</div>
      <div>Houston, TX 77194</div>
      <div>Phone: 713.555.0148</div>
      <div>Daniel@BrenvikInnovations.com</div>
    </div>
    <svg class="wave" viewBox="0 0 532 60" height="60" preserveAspectRatio="none" aria-hidden="true">
      <path d="M0 22 C150 42 330 2 532 18 L532 60 L0 60 Z" fill="var(--grey)"/>
      <path d="M0 32 C160 54 340 14 532 28 L532 60 L0 60 Z" fill="var(--purple)"/>
    </svg>
  </section>

  <section class="sheet letterhead">
    <div class="brand"><span class="brand-mark"></span>Brenvik Innovations</div>
    <div class="letter-contact">
      <span>Phone</span><span>713.555.0148</span>
      <span>Address</span><span>5812-4 Calloway Ave #2267, Houston, TX 77194</span>
      <span>Email</span><span>Daniel@BrenvikInnovations.com</span>
      <span>Web</span><span>BrenvikInnovations.com</span>
    </div>
    <svg class="wave" viewBox="0 0 471 60" height="60" preserveAspectRatio="none" aria-hidden="true">
      <path d="M0 20 C140 42 300 0 471 16 L471 60 L0 60 Z" fill="var(--grey)"/>
      <path d="M0 30 C150 54 310 12 471 26 L471 60 L0 60 Z" fill="var(--purple)"/>
    </svg>
  </section>

  <section class="sheet note note-a">
    <header class="note-header">
      <div class="brand"><span class="brand-mark"></span>Brenvik Innovations</div>
      <span class="note-owner">Daniel Marlow</span>
    </header>
    <svg class="wave" viewBox="0 0 336 50" height="50" preserveAspectRatio="none" aria-hidden="true">
      <path d="M0 16 C100 36 210 0 336 14 L336 50 L0 50 Z" fill="var(--grey)"/>
      <path d="M0 24 C110 46 220 10 336 22 L336 50 L0 50 Z" fill="var(--purple)"/>
    </svg>
  </section>

  <section class="sheet note note-b">
    <header class="note-header">
      <div class="brand"><span class="brand-mark"></span>Brenvik Innovations</div>
      <span class="note-owner">Daniel Marlow</span>
    </header>
    <svg class="wave" viewBox="0 0 336 50" height="50" preserveAspectRatio="none" aria-hidden="true">
      <path d="M0 16 C100 36 210 0 336 14 L336 50 L0 50 Z" fill="var(--grey)"/>
      <path d="M0 24 C110 46 220 10 336 22 L336 50 L0 50 Z" fill="var(--purple)"/>
    </svg>
  </section>

</body>
</html>
```